Brookfarrow Osteopathy and dry needling business card

Business card for Brookfarrow Osteopathy and Dry Needling.

Industry/Entity Type

Health

Contact Information for Business Card

I do not have a phone number yet. I also do not have an email address yet. The physical address is: 48 Lower Crane Street Brookfarrow The website is: www.brookfarrowosteosteopathy.example My details are: Dr Martin Pellowe, Osteopath (B.Clin.Sci (Ost) M.Ost BSC ECON (Hons)

Colors
0094D4
00A9DD
6FCCEA
C7EBF8
E9F6FB

Requirements
Must have
• logo on the back
Nice to have
• Maybe a space for me to write an appointment time and date on the card.

```html
<!DOCTYPE html>
<html lang="en">
<head>
<meta charset="utf-8">
<title>Brookfarrow Osteopathy and Dry Needling – Business Card</title>
<link href="https://fonts.googleapis.com/css2?family=Lato:ital,wght@0,400;0,700;0,900;1,400&display=swap" rel="stylesheet">
<style>
  :root {
    --brand-blue: #1799d4;
    --brand-blue-deep: #0e90d0;
    --accent-orange: #f39325;
    --paper: #ffffff;
    --backdrop: #3a3a3a;
  }
  * { margin: 0; padding: 0; box-sizing: border-box; }
  html, body { width: 1200px; height: 689px; overflow: hidden; }
  body {
    background: var(--backdrop);
    font-family: "Lato", sans-serif;
    position: relative;
  }
  .card {
    position: absolute;
    top: 190px;
    width: 540px;
    height: 310px;
    border-radius: 22px;
    overflow: hidden;
    box-shadow: 0 12px 30px rgba(0,0,0,.45);
  }

  /* Appointment side */
  .appointment { left: 35px; background: var(--brand-blue); color: var(--paper); }
  .appointment__title {
    position: absolute; top: 30px; left: 0; right: 0;
    text-align: center; font-weight: 900; font-size: 30px; letter-spacing: .5px;
  }
  .field {
    position: absolute; height: 40px; border-radius: 20px; background: var(--paper);
    color: var(--brand-blue); font-size: 15px; letter-spacing: 1px;
    display: flex; align-items: center; justify-content: space-between; padding: 0 20px;
  }
  .field--name { top: 86px; left: 30px; right: 30px; }
  .field--date { top: 140px; left: 30px; width: 232px; }
  .field--time { top: 140px; left: 278px; width: 232px; }
  .field__hint { font-size: 11px; }
  .weekdays {
    position: absolute; top: 200px; left: 30px; right: 30px;
    display: flex; justify-content: space-between; font-size: 16px; letter-spacing: .5px;
  }
  .weekday { display: flex; align-items: center; gap: 6px; }
  .weekday__box { width: 13px; height: 13px; background: var(--paper); display: inline-block; }
  .appointment__note {
    position: absolute; top: 246px; left: 40px; right: 40px;
    text-align: center; font-style: italic; font-size: 12.5px; line-height: 1.35;
  }

  /* Contact side */
  .contact { left: 625px; background: var(--paper); }
  .contact__wave { position: absolute; inset: 0; }
  .brand-mark {
    position: absolute; top: 36px; left: 360px; width: 150px;
    display: flex; align-items: center; gap: 8px;
    color: var(--brand-blue); font-weight: 700; font-size: 14px; line-height: 1.25;
  }
  .brand-mark__dot { flex: none; width: 16px; height: 16px; border-radius: 50%; background: var(--brand-blue); }
  .person { position: absolute; left: 28px; top: 148px; color: var(--paper); }
  .person__name { font-weight: 900; font-size: 27px; letter-spacing: .5px; }
  .person__role { font-weight: 700; font-size: 12.5px; margin-top: 3px; }
  .person__rule { width: 190px; height: 1px; background: var(--paper); margin: 10px 0 10px; }
  .contact-list { list-style: none; font-size: 14px; }
  .contact-list li { display: flex; align-items: center; gap: 9px; height: 21px; }
  .contact-list svg { width: 12px; height: 12px; flex: none; }
</style>
</head>
<body>

  <section class="card appointment" aria-label="Appointment card">
    <h2 class="appointment__title">YOUR NEXT APPOINTMENT</h2>
    <div class="field field--name">NAME:</div>
    <div class="field field--date">DATE:</div>
    <div class="field field--time">TIME <span class="field__hint">AM\PM</span></div>
    <div class="weekdays">
      <span class="weekday"><i class="weekday__box"></i>MON</span>
      <span class="weekday"><i class="weekday__box"></i>TUES</span>
      <span class="weekday"><i class="weekday__box"></i>WED</span>
      <span class="weekday"><i class="weekday__box"></i>THU</span>
      <span class="weekday"><i class="weekday__box"></i>FRI</span>
      <span class="weekday"><i class="weekday__box"></i>SAT</span>
    </div>
    <p class="appointment__note">If you are unable to keep your appointment, please call us to<br>re scheduleatleast 48 hours prior to your appointment.</p>
  </section>

  <section class="card contact" aria-label="Contact card">
    <svg class="contact__wave" viewBox="0 0 540 310" preserveAspectRatio="none">
      <path d="M314,0 C300,60 330,105 375,150 C425,198 470,235 482,310" fill="none" stroke="var(--accent-orange)" stroke-width="6"/>
      <path d="M302,0 C288,60 318,105 362,150 C410,198 455,235 468,310 H0 V0 Z" fill="var(--brand-blue-deep)"/>
    </svg>

    <div class="brand-mark">
      <span class="brand-mark__dot"></span>
      <span>Brookfarrow Osteopathy and Dry Needling</span>
    </div>

    <div class="person">
      <h1 class="person__name">DR MARTIN PELLOWE</h1>
      <p class="person__role">Osteopath (B.Clin.Sci (Ost) M.Ost BSC ECON (Hons)</p>
      <div class="person__rule"></div>
      <ul class="contact-list">
        <li><svg viewBox="0 0 24 24"><path fill="#fff" d="M6.6 10.8a15 15 0 0 0 6.6 6.6l2.2-2.2c.3-.3.7-.4 1-.2 1.1.4 2.3.6 3.6.6.6 0 1 .4 1 1V20c0 .6-.4 1-1 1A17 17 0 0 1 3 4c0-.6.4-1 1-1h3.5c.6 0 1 .4 1 1 0 1.3.2 2.5.6 3.6.1.3 0 .7-.2 1z"/></svg>(123) 555-0148</li>
        <li><svg viewBox="0 0 24 24"><path fill="#fff" d="M2 5h20v14H2z"/><path d="M2 5l10 8 10-8" fill="none" stroke="#0e90d0" stroke-width="2"/></svg>info@brookfarrowosteosteopathy.example</li>
        <li><svg viewBox="0 0 24 24"><circle cx="12" cy="12" r="9" fill="none" stroke="#fff" stroke-width="2.5"/><path d="M3 12h18M12 3c3 3 3 15 0 18M12 3c-3 3-3 15 0 18" fill="none" stroke="#fff" stroke-width="1.8"/></svg>brookfarrowosteosteopathy.example</li>
        <li><svg viewBox="0 0 24 24"><path fill="#fff" d="M12 2a7 7 0 0 0-7 7c0 5 7 13 7 13s7-8 7-13a7 7 0 0 0-7-7zm0 9.5A2.5 2.5 0 1 1 12 6.5a2.5 2.5 0 0 1 0 5z"/></svg>48 Lower Crane Street Brookfarrow</li>
      </ul>
    </div>
  </section>

</body>
</html>
```